Professional business cards for real estate development company

I need business cards for my new real estate development company. The company, "KORVA" is a real estate development, investment, and advisory firm with a focus on multifamily, office, and mixed-use projects across primary and secondary markets in the Southeast United States.

Style preference is modern

Industry/Entity Type

Real Estate Development

Contact Information for Business Card

The business cards need to include:
Name
Title
Mailing Address
Phone Number
Web Address

Logo is attached. I would like white to be the primary color with incorporation of the company colors: #232D3A and #B5A451

Font styles to use
Other font styles liked:
• Montserrat, Avenir

Requirements
Must have
• Company Logo. No need to include the company name since the name is in the logo.
Should not have
• No line type designs

```html
<!DOCTYPE html>
<html lang="en">
<head>
<meta charset="UTF-8">
<title>KORVA – Business Cards</title>
<link href="https://fonts.googleapis.com/css2?family=Montserrat:wght@500;600;700;800&display=swap" rel="stylesheet">
<style>
  :root {
    --navy: #232D3A;
    --gold: #B5A451;
    --white: #FFFFFF;
    --stage: #A6A6A6;
    --text: #232D3A;
  }
  * { box-sizing: border-box; margin: 0; padding: 0; }
  html, body {
    width: 1200px; height: 900px; overflow: hidden;
    background: var(--stage);
    font-family: "Montserrat", sans-serif;
  }
  .stage {
    width: 1200px; height: 900px;
    display: flex; flex-direction: column;
    align-items: center; justify-content: center; gap: 40px;
  }
  .card {
    position: relative;
    width: 700px; height: 400px;
    border-radius: 28px;
    overflow: hidden;
  }
  /* Back side */
  .card--back {
    background: var(--navy);
    display: flex; align-items: center; justify-content: center;
  }
  .wordmark {
    display: flex; align-items: center; gap: 16px;
    font-weight: 700; letter-spacing: 6px;
    white-space: nowrap;
  }
  .wordmark__square { width: 34px; height: 34px; flex: none; }
  .card--back .wordmark { color: var(--white); font-size: 72px; }
  .card--back .wordmark__square { background: var(--white); }

  /* Front side */
  .card--front { background: var(--white); }
  .card__wave { position: absolute; inset: 0; width: 100%; height: 100%; }
  .card--front .wordmark {
    position: absolute; left: 62px; top: 168px;
    color: var(--navy); font-size: 48px; letter-spacing: 4px;
  }
  .card--front .wordmark__square { width: 24px; height: 24px; background: var(--navy); }
  .divider {
    position: absolute; left: 360px; top: 70px;
    width: 2px; height: 170px; background: var(--gold);
  }
  .contact {
    position: absolute; left: 386px; top: 62px;
    color: var(--text);
  }
  .contact__name {
    color: var(--gold); font-weight: 800; font-size: 26px; letter-spacing: 0.5px;
  }
  .contact__title {
    font-weight: 600; font-size: 13px; letter-spacing: 0.5px; margin-top: 2px;
  }
  .contact__address {
    font-weight: 500; font-size: 13.5px; line-height: 1.3; margin-top: 12px;
  }
  .contact__list { list-style: none; margin-top: 12px; }
  .contact__item {
    display: flex; align-items: center; gap: 10px;
    font-weight: 500; font-size: 14px; line-height: 1.75;
    white-space: nowrap;
  }
  .contact__icon { width: 13px; height: 13px; flex: none; fill: var(--gold); }
</style>
</head>
<body>
<main class="stage">
  <section class="card card--back" aria-label="Business card back">
    <div class="wordmark"><span class="wordmark__square"></span>KORVA</div>
  </section>

  <section class="card card--front" aria-label="Business card front">
    <svg class="card__wave" viewBox="0 0 700 400" preserveAspectRatio="none" aria-hidden="true">
      <path d="M150 400 C 380 380, 470 300, 700 270 L 700 400 Z" fill="var(--gold)"/>
      <path d="M175 400 C 400 384, 485 310, 700 280 L 700 400 Z" fill="var(--white)"/>
      <path d="M200 400 C 420 388, 500 318, 700 288 L 700 400 Z" fill="var(--navy)"/>
    </svg>

    <div class="wordmark"><span class="wordmark__square"></span>KORVA</div>

    <div class="divider"></div>

    <div class="contact">
      <p class="contact__name">DANIEL REEVE</p>
      <p class="contact__title">MANAGING DIRECTOR</p>
      <p class="contact__address">118 Peachtree Lane,<br>Atlanta, Georgia - 30303</p>
      <ul class="contact__list">
        <li class="contact__item">
          <svg class="contact__icon" viewBox="0 0 24 24"><path d="M6.6 10.8a15.1 15.1 0 0 0 6.6 6.6l2.2-2.2a1 1 0 0 1 1-.25 11.4 11.4 0 0 0 3.6.57 1 1 0 0 1 1 1V20a1 1 0 0 1-1 1A17 17 0 0 1 3 4a1 1 0 0 1 1-1h3.5a1 1 0 0 1 1 1c0 1.25.2 2.45.57 3.57a1 1 0 0 1-.25 1z"/></svg>
          404-555-0182
        </li>
        <li class="contact__item">
          <svg class="contact__icon" viewBox="0 0 24 24"><path d="M2 5h20v14H2z"/><path d="M3 6l9 7 9-7" fill="none" stroke="var(--white)" stroke-width="1.5"/></svg>
          hello@korvadev.com
        </li>
        <li class="contact__item">
          <svg class="contact__icon" viewBox="0 0 24 24"><circle cx="12" cy="12" r="10"/><path d="M2 12h20M12 2c3 3 3 17 0 20M12 2c-3 3-3 17 0 20" fill="none" stroke="var(--white)" stroke-width="1.4"/></svg>
          www.korvadev.com
        </li>
      </ul>
    </div>
  </section>
</main>
</body>
</html>
```